Brochure Design Project

I need a presentation folder with two inside pages and a pocket on back cover, use use my logo ,
make the cover just using the logo (put it big and centered, then use the logo in the background to fill, read the brief and make it modern, stop trying to make it exactly like the picture I gave as sample please use your talent trust your self
I just uploaded text for presentation folder
Target Market(s)
Dr's offices and patients

```html
<!DOCTYPE html>
<html lang="en">
<head>
<meta charset="UTF-8">
<title>VitaPath Counseling – Presentation Folder Inside Spread</title>
<link href="https://fonts.googleapis.com/css2?family=Montserrat:ital,wght@0,400;0,500;0,600;0,700;1,600;1,700&display=swap" rel="stylesheet">
<style>
  :root{
    --bg-top:#5a5a5a;
    --bg-bottom:#2e2e2e;
    --paper:#f3f3f3;
    --paper-shade:#e6e6e6;
    --pocket:#e9e9e9;
    --brown:#5a3316;
    --brown-mid:#7b4a24;
    --orange:#b8651c;
    --ink:#555555;
    --ink-dark:#3a3a3a;
    --card:#a08b7a;
    --photo-warm-a:#d9cfc6;
    --photo-warm-b:#b99b86;
    --photo-sky-a:#cfe3f2;
    --photo-sky-b:#8fb6d8;
  }
  *{box-sizing:border-box;margin:0;padding:0}
  html,body{width:1200px;height:1000px;overflow:hidden}
  body{
    background:linear-gradient(180deg,var(--bg-top),var(--bg-bottom));
    font-family:"Montserrat",sans-serif;
    color:var(--ink);
    position:relative;
  }
  .spread{
    position:absolute;left:60px;top:140px;width:1080px;height:720px;
    display:flex;box-shadow:0 20px 50px rgba(0,0,0,.45);
  }
  .page{position:relative;width:540px;height:720px;background:var(--paper);overflow:hidden}
  .page--left{background:linear-gradient(90deg,var(--paper) 85%,var(--paper-shade))}
  .page--right{background:linear-gradient(90deg,var(--paper-shade),var(--paper) 15%)}
  .abs{position:absolute}

  .intro-title{left:40px;top:44px;font-size:22px;font-weight:700;color:var(--orange)}
  .intro-title span{font-weight:500}
  .body-copy{font-size:9px;line-height:1.4;color:var(--ink)}
  .body-copy p+p{margin-top:7px}
  .intro-copy{left:40px;top:80px;width:245px}
  .detail-copy{left:310px;top:258px;width:205px}

  .photo{background:linear-gradient(135deg,var(--photo-warm-a),var(--photo-warm-b))}
  .photo--family-small{left:305px;top:70px;width:215px;height:170px;border-radius:6px}
  .photo--family-large{left:20px;top:270px;width:270px;height:200px;border-radius:6px}

  .about{left:40px;top:520px;width:460px}
  .about h2{font-size:15px;font-weight:700;color:var(--orange);margin-bottom:5px}
  .about p{font-size:9.5px;font-weight:700;line-height:1.45;color:var(--ink-dark)}
  .swoosh{left:0;top:610px;width:540px;height:110px}

  .tab{height:24px;background:linear-gradient(90deg,var(--brown),var(--brown-mid));
    color:#fff;font-size:12.5px;font-weight:700;padding:5px 12px;border-radius:0 12px 12px 0;
    display:flex;align-items:center;gap:8px}
  .tab::after{content:"";width:9px;height:9px;border-radius:50%;background:#fff;opacity:.85;margin-left:auto}
  .tab--services{left:28px;top:140px;width:220px}
  .tab--opioid{left:290px;top:168px;width:220px}
  .list{list-style:none;font-size:8.5px;line-height:1.3;color:var(--ink-dark)}
  .list li{display:flex;gap:5px;margin-bottom:5px}
  .list svg{flex:none;margin-top:2px}
  .list--services{left:32px;top:174px;width:215px;font-weight:600}
  .list--opioid{left:294px;top:202px;width:215px;font-weight:600}
  .list--opioid li{margin-bottom:3px}

  .photo--couple{left:36px;top:402px;width:190px;height:88px;border-radius:40px 14px 40px 14px;
    background:linear-gradient(180deg,var(--photo-sky-a),var(--photo-sky-b));border:3px solid var(--brown-mid)}
  .photo--man{left:300px;top:350px;width:220px;height:150px;
    background:linear-gradient(180deg,var(--paper),var(--photo-warm-a) 40%,var(--photo-sky-a))}

  .pocket{left:0;top:500px;width:540px;height:220px;background:var(--pocket);
    box-shadow:0 -4px 10px rgba(0,0,0,.12)}
  .brand{left:40px;top:28px;display:flex;align-items:center;gap:8px;
    font-size:22px;font-weight:600;color:var(--brown-mid)}
  .brand::before{content:"";width:14px;height:14px;border-radius:50%;background:var(--brown-mid)}
  .stat{left:40px;top:78px;width:200px;font-size:10px;font-weight:700;font-style:italic;
    line-height:1.4;color:var(--orange)}
  .card-slot{left:275px;top:70px;width:215px;height:120px;background:var(--card);
    display:flex;align-items:center;justify-content:center;font-size:9px;color:var(--ink-dark)}
  .slit{left:260px;top:55px;width:245px;height:150px}
</style>
</head>
<body>
<main class="spread">
  <section class="page page--left">
    <h1 class="abs intro-title">VitaPath <span>Counseling</span></h1>
    <div class="abs body-copy intro-copy">
      <p>VitaPath Counseling is a proactive addiction counseling service dedicated to helping clinics and physicians reduce the misuse of prescribed pain medications. Our counselors work alongside medical teams to educate patients, guide safe medication use and support better outcomes for every person in care.</p>
      <p>VitaPath Counseling will provide education and prevention services to patients who are prescribed medications for health related reasons, to prevent possible substance use disorders.</p>
    </div>
    <div class="abs photo photo--family-small" role="img" aria-label="Photo of a smiling family with two young children sitting together"></div>
    <div class="abs photo photo--family-large" role="img" aria-label="Photo of a smiling young family of four posing close together"></div>
    <div class="abs body-copy detail-copy">
      <p>VitaPath Counseling will receive referrals from pain management clinics to address this growing issue in healthcare.</p>
      <p>VitaPath Counseling services are provided by addiction professionals experienced in addiction education and prevention.</p>
      <p>Many pain management physicians are interested in reducing risk to their practice and increasing quality care for their patients.</p>
      <p>VitaPath Counseling will provide education and screening to help patients understand the risks of opioid misuse.</p>
      <p>VitaPath Counseling will provide education, prevention, screening, assessments and referrals for chronic pain and substance use disorders.</p>
    </div>
    <div class="abs about">
      <h2>VitaPath Counseling Is !</h2>
      <p>VitaPath's Dedicated Counselors exude a contagious interest in the life of our patients, within an intimately scaled caring environment that engenders transformative learning. We're dedicated to informing and educating lives where every patient is treated as a person with individual needs by professional, caring staff</p>
    </div>
    <svg class="abs swoosh" viewBox="0 0 540 110" aria-hidden="true">
      <path d="M0 5 C140 55 330 80 540 95 L540 110 L0 110 Z" fill="#ececec"/>
      <path d="M0 5 C140 55 330 80 540 95" fill="none" stroke="#7b4a24" stroke-width="3"/>
      <path d="M0 20 C140 70 330 95 540 108" fill="none" stroke="#b8651c" stroke-width="1.5"/>
    </svg>
  </section>

  <section class="page page--right">
    <h2 class="abs tab tab--services">Services offered</h2>
    <ul class="abs list list--services">
      <li><svg width="7" height="7" viewBox="0 0 8 8"><path d="M1 7 L7 1 M3 1 H7 V5" stroke="#7b4a24" stroke-width="1.4" fill="none"/></svg>Pro active opioid education</li>
      <li><svg width="7" height="7" viewBox="0 0 8 8"><path d="M1 7 L7 1 M3 1 H7 V5" stroke="#7b4a24" stroke-width="1.4" fill="none"/></svg>Education materials to inform patients about the risk of taking medications inappropriately.</li>
      <li><svg width="7" height="7" viewBox="0 0 8 8"><path d="M1 7 L7 1 M3 1 H7 V5" stroke="#7b4a24" stroke-width="1.4" fill="none"/></svg>Prevention services to educate patients about the risk and warning symptoms of substance misuse and abuse</li>
      <li><svg width="7" height="7" viewBox="0 0 8 8"><path d="M1 7 L7 1 M3 1 H7 V5" stroke="#7b4a24" stroke-width="1.4" fill="none"/></svg>Screening for potential substance use disorders related to prescribed medications</li>
      <li><svg width="7" height="7" viewBox="0 0 8 8"><path d="M1 7 L7 1 M3 1 H7 V5" stroke="#7b4a24" stroke-width="1.4" fill="none"/></svg>Assessment for substance use disorders related to medical issues and prescribed medications</li>
      <li><svg width="7" height="7" viewBox="0 0 8 8"><path d="M1 7 L7 1 M3 1 H7 V5" stroke="#7b4a24" stroke-width="1.4" fill="none"/></svg>Counseling provided by experienced addiction professionals to address substance related misuse and abuse for patients taking prescribed medications.</li>
    </ul>
    <h2 class="abs tab tab--opioid">Opioid Education</h2>
    <ul class="abs list list--opioid">
      <li><svg width="7" height="7" viewBox="0 0 8 8"><path d="M7 7 L1 1 M5 1 H1 V5" stroke="#7b4a24" stroke-width="1.4" fill="none"/></svg>Opioid Education</li>
      <li><svg width="7" height="7" viewBox="0 0 8 8"><path d="M7 7 L1 1 M5 1 H1 V5" stroke="#7b4a24" stroke-width="1.4" fill="none"/></svg>Using Opioids safely</li>
      <li><svg width="7" height="7" viewBox="0 0 8 8"><path d="M7 7 L1 1 M5 1 H1 V5" stroke="#7b4a24" stroke-width="1.4" fill="none"/></svg>The Role of Medications</li>
      <li><svg width="7" height="7" viewBox="0 0 8 8"><path d="M7 7 L1 1 M5 1 H1 V5" stroke="#7b4a24" stroke-width="1.4" fill="none"/></svg>Opioid Agreements and Contracts</li>
      <li><svg width="7" height="7" viewBox="0 0 8 8"><path d="M7 7 L1 1 M5 1 H1 V5" stroke="#7b4a24" stroke-width="1.4" fill="none"/></svg>Responsible Use</li>
      <li><svg width="7" height="7" viewBox="0 0 8 8"><path d="M7 7 L1 1 M5 1 H1 V5" stroke="#7b4a24" stroke-width="1.4" fill="none"/></svg>Storing Medication</li>
      <li><svg width="7" height="7" viewBox="0 0 8 8"><path d="M7 7 L1 1 M5 1 H1 V5" stroke="#7b4a24" stroke-width="1.4" fill="none"/></svg>Alcohol &amp; Marijuana and Pain Medication</li>
      <li><svg width="7" height="7" viewBox="0 0 8 8"><path d="M7 7 L1 1 M5 1 H1 V5" stroke="#7b4a24" stroke-width="1.4" fill="none"/></svg>Over the Counter Medication</li>
      <li><svg width="7" height="7" viewBox="0 0 8 8"><path d="M7 7 L1 1 M5 1 H1 V5" stroke="#7b4a24" stroke-width="1.4" fill="none"/></svg>Storing your Medication Safely</li>
    </ul>
    <div class="abs photo--couple" role="img" aria-label="Photo of a smiling senior couple against a blue sky"></div>
    <div class="abs photo--man" role="img" aria-label="Photo of a smiling man in a light blue shirt with arms crossed"></div>

    <div class="abs pocket">
      <div class="abs brand">VitaPath Counseling</div>
      <p class="abs stat">According to the Northfield Medical Society More than 76 million Americans are Suffering with Chronic Pain. Pro Active Addiction Counseling Is Needed and No One Is Providing This Service!</p>
      <div class="abs card-slot">Space for business cards</div>
      <svg class="abs slit" viewBox="0 0 245 150" aria-hidden="true">
        <path d="M5 30 L60 5" stroke="#333" stroke-width="1" stroke-dasharray="4 3" fill="none"/>
        <path d="M185 145 L240 120" stroke="#333" stroke-width="1" stroke-dasharray="4 3" fill="none"/>
      </svg>
    </div>
  </section>
</main>
</body>
</html>
```